Business card to be used as a flyer

This business card should do the trick of a full scale flyer , so basicaly from the business card itself we only keep the size and remove the clasical name , position , company name (etc).
This business cards should be , like said above, used as promo tool, being gived to different girls . So base one : the design is girls oriented.
Colors : black background . We will use gold (color) folio for the text.
Attached you have our logo, but this should not be a proiminent part of the design . You can use only the cat head instead.
Target Market(s)
Girls / Women
Contact Information for Business Card
> black background , gold / folio text and elements
> cat head from the logo in a creative way do be displayed
> proieminent text "your path to success starts here"
> contact details phone and website .
www.velmastrand.ro (website) and 0742163958 (phone)

```html
<!DOCTYPE html>
<html lang="en">
<head>
<meta charset="UTF-8">
<title>Velmastrand Promo Card</title>
<link rel="stylesheet" href="https://fonts.googleapis.com/css2?family=Dancing+Script:wght@600&family=Poppins:wght@500&display=swap">
<style>
  :root {
    --backdrop: #262626;
    --card: #1c1c1c;
    --card-edge: #2e2e2e;
    --gold: #e0a91c;
    --gold-light: #f7d155;
  }
  html, body {
    margin: 0;
    padding: 0;
    width: 902px;
    height: 1200px;
    overflow: hidden;
    background: var(--backdrop);
  }
  .sheet {
    position: relative;
    width: 902px;
    height: 1200px;
    display: flex;
    flex-direction: column;
    align-items: center;
    justify-content: space-around;
  }
  .card {
    position: relative;
    width: 640px;
    height: 366px;
    background: var(--card);
    border: 1px solid var(--card-edge);
    border-radius: 4px;
    box-shadow: 0 18px 40px rgba(0,0,0,0.45);
  }
  .gold-foil {
    background: linear-gradient(100deg, var(--gold) 0%, var(--gold-light) 45%, var(--gold) 100%);
    -webkit-background-clip: text;
    background-clip: text;
    color: transparent;
  }
  .card-front .tagline {
    position: absolute;
    left: 0;
    right: 0;
    top: 158px;
    margin: 0;
    text-align: center;
    font-family: "Dancing Script", cursive;
    font-weight: 600;
    font-size: 38px;
    letter-spacing: 0.5px;
  }
  .card-back .contact-block {
    position: absolute;
    left: 44px;
    bottom: 44px;
    display: flex;
    align-items: center;
    gap: 18px;
    font-family: "Poppins", sans-serif;
    font-weight: 500;
  }
  .brand-name {
    font-size: 17px;
    color: var(--gold);
    letter-spacing: 0.5px;
  }
  .contact-list {
    list-style: none;
    margin: 0;
    padding: 0;
    display: flex;
    flex-direction: column;
    gap: 6px;
  }
  .contact-item {
    display: flex;
    align-items: center;
    gap: 7px;
    font-size: 13px;
    color: var(--gold);
  }
  .contact-item svg {
    width: 12px;
    height: 12px;
    flex: none;
  }
</style>
</head>
<body>
<main class="sheet">
  <section class="card card-front">
    <p class="tagline gold-foil">Your path to success starts here</p>
  </section>

  <section class="card card-back">
    <div class="contact-block">
      <span class="brand-name">Velmastrand</span>
      <ul class="contact-list">
        <li class="contact-item">
          <svg viewBox="0 0 24 24" aria-hidden="true"><path fill="#e0a91c" d="M6.6 10.8a15.1 15.1 0 0 0 6.6 6.6l2.2-2.2c.3-.3.7-.4 1-.2 1.1.4 2.3.6 3.6.6.6 0 1 .4 1 1V20c0 .6-.4 1-1 1A17 17 0 0 1 3 4c0-.6.4-1 1-1h3.5c.6 0 1 .4 1 1 0 1.3.2 2.5.6 3.6.1.3 0 .7-.2 1z"/></svg>
          0742163958
        </li>
        <li class="contact-item">
          <svg viewBox="0 0 24 24" aria-hidden="true" fill="none" stroke="#e0a91c" stroke-width="2"><circle cx="12" cy="12" r="9"/><path d="M3 12h18M12 3c3 3 3 15 0 18M12 3c-3 3-3 15 0 18"/></svg>
          www.velmastrand.ro
        </li>
      </ul>
    </div>
  </section>
</main>
</body>
</html>
```